Wow me with your Earring card options!

An A7 portrait sized earring card is required for Velvet & Vinyl. Inspired by Velvet and fueled by Vinyl we love our accessories to do the talking. Bold statement earrings are our thing. Our earring cards need to showcase our brand while not stealing all of the limelight from the earrings themselves. Earring care information needs to be included on the back side of the card. Our simple logo needs to be the basis for the colour choices used on the card.

Need extra days to review

• No florals please 😊

```html
<!DOCTYPE html>
<html lang="en">
<head>
<meta charset="utf-8">
<title>Velvet &amp; Vinyl – Earring Cards</title>
<link href="https://fonts.googleapis.com/css2?family=Lato:wght@400;900&display=swap" rel="stylesheet">
<style>
  :root {
    --stage: #0b023a;
    --ink: #1c1a22;
    --logo: #5b5466;
    --grad-purple: #a49ac8;
    --grad-pink: #d4a3b2;
    --grad-peach: #f3ad86;
    --grad-yellow: #f8eeb0;
    --grad-green: #a8d49b;
    --grad-teal: #78b0b3;
  }
  html, body {
    margin: 0;
    padding: 0;
    width: 1200px;
    height: 1200px;
    overflow: hidden;
    background: var(--stage);
    font-family: "Lato", sans-serif;
  }
  .canvas {
    position: relative;
    width: 1200px;
    height: 1200px;
  }
  .card {
    position: absolute;
    width: 496px;
    height: 696px;
    background: linear-gradient(180deg,
      var(--grad-purple) 0%,
      var(--grad-pink) 20%,
      var(--grad-peach) 40%,
      var(--grad-yellow) 56%,
      var(--grad-green) 78%,
      var(--grad-teal) 100%);
    box-shadow: 0 12px 26px rgba(0, 0, 0, 0.45);
    color: var(--ink);
  }
  .card--front { left: 80px; top: 130px; }
  .card--back  { left: 625px; top: 373px; }

  .wordmark {
    position: absolute;
    left: 0;
    right: 0;
    text-align: center;
    font-weight: 900;
    font-size: 44px;
    letter-spacing: 1px;
    color: var(--logo);
  }
  .card--front .wordmark { top: 322px; }
  .card--back .wordmark { top: 128px; }

  .care-list {
    position: absolute;
    left: 60px;
    top: 252px;
    margin: 0;
    padding: 0;
    list-style: none;
  }
  .care-list li {
    display: flex;
    align-items: center;
    height: 35px;
    font-size: 18.5px;
  }
  .care-list svg, .contact-box svg {
    width: 26px;
    height: 26px;
    fill: none;
    stroke: var(--ink);
    stroke-width: 1.2;
    flex: none;
  }
  .care-list svg { margin-right: 24px; }

  .contact-box {
    position: absolute;
    left: 68px;
    top: 420px;
    width: 358px;
    height: 125px;
    box-sizing: border-box;
    border: 2px solid var(--ink);
    border-radius: 20px;
    padding: 12px 0 0 27px;
  }
  .contact-box div {
    display: flex;
    align-items: center;
    height: 33.5px;
    font-size: 17.5px;
  }
  .contact-box svg { margin-right: 22px; }

  .social-row {
    position: absolute;
    left: 0;
    right: 0;
    top: 588px;
    display: flex;
    justify-content: center;
    gap: 16px;
    font-size: 14px;
  }
  .social-row span {
    display: flex;
    align-items: center;
  }
  .social-row span::before {
    content: "";
    width: 12px;
    height: 12px;
    background: var(--ink);
    border-radius: 2px;
    margin-right: 6px;
  }
</style>
</head>
<body>
<main class="canvas">

  <section class="card card--front" aria-label="Earring card front">
    <div class="wordmark">Velvet &amp; Vinyl</div>
  </section>

  <section class="card card--back" aria-label="Earring card back">
    <div class="wordmark">Velvet &amp; Vinyl</div>

    <ul class="care-list">
      <li>
        <svg viewBox="0 0 26 26" aria-hidden="true"><path d="M9 8 C6 13 4 15 4 18 a5 5 0 0 0 10 0 C14 15 12 13 9 8Z"/><path d="M18 3 C16 6 15 7 15 9 a3 3 0 0 0 6 0 C21 7 20 6 18 3Z"/></svg>
        Avoid moisture &amp; remove before bathing
      </li>
      <li>
        <svg viewBox="0 0 26 26" aria-hidden="true"><rect x="3" y="12" width="20" height="6" rx="1"/><rect x="6" y="8" width="6" height="4" rx="1"/><rect x="14" y="8" width="6" height="4" rx="1"/><path d="M4 18v3M22 18v3M4 12V7h18v5"/></svg>
        For comforts sake, remove before bed!
      </li>
      <li>
        <svg viewBox="0 0 26 26" aria-hidden="true"><ellipse cx="11" cy="18" rx="7" ry="6"/><rect x="9" y="8" width="4" height="4"/><path d="M11 8V4h5"/><circle cx="19" cy="4" r="2"/></svg>
        Avoid contact with perfume &amp; lotions
      </li>
      <li>
        <svg viewBox="0 0 26 26" aria-hidden="true"><circle cx="13" cy="13" r="5"/><path d="M13 2v4M13 20v4M2 13h4M20 13h4M5 5l3 3M18 18l3 3M5 21l3-3M18 8l3-3"/></svg>
        Store away from direct sunlight
      </li>
    </ul>

    <div class="contact-box">
      <div>
        <svg viewBox="0 0 26 26" aria-hidden="true"><circle cx="13" cy="13" r="10"/><ellipse cx="13" cy="13" rx="4.5" ry="10"/><path d="M3 13h20M5 8h16M5 18h16"/></svg>
        www.velvetandvinyl.com.au
      </div>
      <div>
        <svg viewBox="0 0 26 26" aria-hidden="true"><rect x="2" y="9" width="22" height="14"/><path d="M2 9l11 8 11-8M2 23l8-7M24 23l-8-7"/><circle cx="13" cy="5" r="3"/></svg>
        hello@velvetandvinyl.com.au
      </div>
      <div>
        <svg viewBox="0 0 26 26" aria-hidden="true"><circle cx="13" cy="13" r="11"/><circle cx="13" cy="10" r="4"/><path d="M5.5 21c2-4 5-5 7.5-5s5.5 1 7.5 5"/></svg>
        @velvetandvinyl
      </div>
    </div>

    <nav class="social-row" aria-label="Social channels">
      <span>Reelo</span>
      <span>Pinwell</span>
      <span>Friendly</span>
      <span>Photoly</span>
    </nav>
  </section>

</main>
</body>
</html>
```